RevelHubQZ Business Cards

Front
Has logo with a design. Website address (www.revelhubqz.example)
Has slogan (discover nightlife)
Has phone number (5129873304)
Should be bold and stands out.

Back
Has details about what we offer.

Events
Search upcoming events
Submit events
Party Image Gallery
View and download HQ party images
Sign up as a contributing event photographer and get paid!
Tickets
Sell your event tickets online for free!
Direct pay
No ticket fee

Target Market(s)

These cards will be handed out in clubs and events to patrons.

Industry/Entity Type

Business

Contact Information for Business Card

Should match or mirror our website in some sort of way. Visit the website to get ideas.

Requirements
Must have
• Must be designed for a 3x3 inch card.

```html
<!DOCTYPE html>
<html lang="en">
<head>
<meta charset="utf-8">
<title>RevelHubQZ Business Cards</title>
<link href="https://fonts.googleapis.com/css2?family=Arimo:wght@400;700&display=swap" rel="stylesheet">
<style>
  :root {
    --stage: #c9c9c9;
    --card: #fbfbfb;
    --brand-blue: #3ea6d8;
    --ink: #2b2b2b;
    --muted: #555555;
    --bullet: #7cc1e6;
  }
  * { box-sizing: border-box; margin: 0; padding: 0; }
  html, body {
    width: 1200px; height: 1200px; overflow: hidden;
    background: var(--stage);
    font-family: "Arimo", Arial, sans-serif;
  }
  .sheet {
    width: 1200px; height: 1200px;
    display: flex; align-items: center; justify-content: center;
    gap: 40px;
  }
  .card {
    position: relative;
    width: 540px; height: 540px;
    background: var(--card);
    box-shadow: 0 6px 18px rgba(0,0,0,0.18);
  }
  .brand {
    position: absolute; left: 0; right: 0;
    display: flex; flex-direction: column; align-items: center;
  }
  .brand-row { display: flex; align-items: center; gap: 12px; }
  .brand-mark {
    width: 38px; height: 38px; border-radius: 50%;
    background: var(--brand-blue);
  }
  .brand-name {
    font-size: 44px; font-weight: 400; color: var(--brand-blue);
    letter-spacing: -1px; line-height: 1;
  }
  .brand-slogan {
    margin-top: 8px;
    font-size: 15px; color: var(--muted); letter-spacing: 4px;
  }
  .card-back .brand { top: 160px; }
  .offer-list { list-style: none; position: absolute; }
  .offer-list li {
    display: flex; align-items: center; gap: 10px;
    font-size: 16px; color: var(--muted); line-height: 30px;
  }
  .offer-list li::before {
    content: ""; width: 11px; height: 11px; background: var(--bullet); flex: none;
  }
  .offer-list--extra { right: 40px; top: 44px; }
  .offer-list--extra li { flex-direction: row-reverse; }
  .offer-list--main { left: 48px; top: 300px; }
  .card-front .brand { top: 170px; }
  .contact {
    position: absolute; left: 0; right: 0; top: 320px;
    text-align: center; color: var(--ink);
  }
  .contact-phone { font-size: 20px; }
  .contact-web { font-size: 20px; margin-top: 30px; }
</style>
</head>
<body>
<main class="sheet">
  <section class="card card-back" aria-label="Card back">
    <ul class="offer-list offer-list--extra">
      <li>Search upcoming events</li>
      <li>Party Image Gallery</li>
    </ul>
    <div class="brand">
      <div class="brand-row">
        <span class="brand-mark"></span>
        <span class="brand-name">RevelHubQZ</span>
      </div>
      <span class="brand-slogan">discover nightlife</span>
    </div>
    <ul class="offer-list offer-list--main">
      <li>Events</li>
      <li>Tickets</li>
      <li>Direct pay</li>
      <li>No ticket fee</li>
      <li>Submit events</li>
    </ul>
  </section>

  <section class="card card-front" aria-label="Card front">
    <div class="brand">
      <div class="brand-row">
        <span class="brand-mark"></span>
        <span class="brand-name">RevelHubQZ</span>
      </div>
      <span class="brand-slogan">discover nightlife</span>
    </div>
    <div class="contact">
      <p class="contact-phone">5129873304</p>
      <p class="contact-web">www.revelhubqz.example</p>
    </div>
  </section>
</main>
</body>
</html>
```